依頼詳細
現在、お店のロゴはあります。既存のロゴを使用して、立て看板を新しくしたいと思っています。看板の入稿に必要なデザインをillustratorで作成して頂きたいと思います。
重視するポイントは、
1。概要、特徴にも記載しましたが2Fとわかること。
2.ワインはそうですが、お食事ができること。
3.現在使用しているロゴを看板の中心にもっていってワインと一目でわかるようにしたい
4.現在の立て看板がとてもカジュアルな為、店内の雰囲気とかなりギャップがあります。若年の方が立ち飲みバルや、居酒屋、カフェ等と間違えて誤って入ってこられることがたまにあります。お店の雰囲気がでるようなシンプルで雰囲気のあるデザインを希望します。看板製作会社が、完全データの支給を要求しているため、Adobe Illustratorアウトラインデータ Mac=8.0 Win=CSにて納品お願いします。
お店の雰囲気、現在の看板、ロゴなどは添付ファイル参照ください。
記載項目
店舗名、2F、ワインとお食事、今のロゴ。定番メニューのリスト、電話番号。席数。
希望イメージ
シンプル 複雑
単色 カラフル
暗い 明るい
日常 高級
遊び心 厳粛
未来的 伝統的
女性的 男性的
希望する色
白、ワインレッド系、ロゴに合わせたカラー
納品ファイル
• 高解像度JPG (.jpg)
• イラストレーター形式 (.ai)
補足説明
入口の間口が狭いために、看板に必ず2F+↑を記載していただきたいです。表、左上がり、裏、右上がりの☝をつけてほしいです。現在の立て看板ファイルを参照してください。
看板仕上がりサイズはW600×H900です。【画面有効サイズ】 W530×H830mmとなっています。内側に投光機を設置し、ライトアップされます。宜しくお願いいたします。
■ 選んだ理由

現在の問題点をクリアし、お店の雰囲気が看板一つで出ている所。

■ 提案者全員のお礼・コメント

修正等にご対応いただきまして誠にありがとうございました。今後も名刺の修正等依頼していくつもりですので機会がありましたら是非とも宜しくお願いいたします。

```html
<!DOCTYPE html>
<html lang="ja">
<head>
<meta charset="utf-8">
<title>VELMONT 立て看板</title>
<link href="https://fonts.googleapis.com/css2?family=Noto+Sans+JP:wght@400;500;700;900&display=swap" rel="stylesheet">
<style>
  :root {
    --wine: #c0141c;
    --wine-deep: #a80f16;
    --paper: #ffffff;
    --ink: #6b3a25;
  }
  * { margin: 0; padding: 0; box-sizing: border-box; }
  html, body { width: 802px; height: 1200px; overflow: hidden; background: var(--paper); }
  .sign {
    position: relative;
    width: 802px; height: 1200px;
    background: var(--paper);
    font-family: "Noto Sans JP", sans-serif;
    overflow: hidden;
  }
  .bands { position: absolute; inset: 0; }
  .floor {
    position: absolute; left: 34px; top: 44px;
    display: flex; align-items: center; gap: 18px;
    color: var(--paper);
  }
  .floor-label { font-size: 96px; font-weight: 700; line-height: 1; letter-spacing: 2px; }
  .seats {
    position: absolute; left: 664px; top: 48px;
    width: 132px; height: 132px; border-radius: 50%;
    background: var(--paper); color: var(--wine);
    display: flex; flex-direction: column; align-items: center; justify-content: center;
    font-size: 15px; font-weight: 500; line-height: 1.35; text-align: center;
  }
  .brand {
    position: absolute; left: 0; right: 0; top: 395px;
    display: flex; flex-direction: column; align-items: center;
  }
  .brand-tag { font-size: 30px; font-weight: 500; color: var(--wine); letter-spacing: 3px; margin-left: 150px; }
  .brand-row { display: flex; align-items: center; gap: 26px; margin-top: 4px; }
  .brand-dot { width: 46px; height: 46px; border-radius: 50%; background: var(--ink); }
  .brand-name { font-size: 108px; font-weight: 700; color: var(--ink); line-height: 1; letter-spacing: 2px; }
  .menu {
    position: absolute; left: 80px; top: 712px; width: 520px;
    color: var(--paper); font-size: 18px; line-height: 1.55;
  }
  .menu-list { list-style: none; margin-bottom: 20px; }
  .menu-list li { display: flex; justify-content: space-between; }
  .menu-list .price { width: 130px; }
  .menu-note { margin-bottom: 18px; font-size: 17px; }
  .tagline {
    position: absolute; left: 80px; top: 1010px;
    color: var(--paper); font-size: 28px; font-weight: 500; letter-spacing: 1px;
  }
  .phone {
    position: absolute; left: 70px; top: 1062px;
    display: flex; align-items: center; gap: 8px;
    color: var(--paper); font-size: 58px; font-weight: 700; letter-spacing: 1px;
  }
</style>
</head>
<body>
<main class="sign">
  <svg class="bands" width="802" height="1200" viewBox="0 0 802 1200" aria-hidden="true">
    <path d="M0 0H802V300C640 300 520 370 380 350C230 330 120 300 0 335Z" fill="var(--wine)"/>
    <path d="M0 318C120 288 230 318 380 338C520 358 640 290 802 285" fill="none" stroke="var(--paper)" stroke-width="4"/>
    <path d="M0 650C150 690 300 700 430 690C580 675 700 640 802 630V1200H0Z" fill="var(--wine)"/>
    <path d="M0 670C150 706 300 716 430 706C580 691 700 656 802 646" fill="none" stroke="var(--wine-deep)" stroke-width="6"/>
  </svg>

  <div class="floor">
    <svg width="62" height="62" viewBox="0 0 62 62" aria-label="上向き矢印">
      <circle cx="31" cy="31" r="28" fill="none" stroke="currentColor" stroke-width="4"/>
      <path d="M31 12L45 30H36V50H26V30H17Z" fill="currentColor"/>
    </svg>
    <span class="floor-label">2F</span>
  </div>

  <div class="seats">
    <span>カウンター</span>
    <span>テーブル合わせ</span>
    <span>最大17席</span>
  </div>

  <div class="brand">
    <span class="brand-tag">WINE &amp; DINE</span>
    <div class="brand-row">
      <span class="brand-dot"></span>
      <span class="brand-name">VELMONT</span>
    </div>
  </div>

  <section class="menu">
    <ul class="menu-list">
      <li><span>グラスシャンパーニュ</span><span class="price">¥1,300～</span></li>
      <li><span>グラススパークリング</span><span class="price">¥950～</span></li>
      <li><span>グラスワイン(白・赤) 各種</span><span class="price">¥900～</span></li>
      <li><span>ボトル各種</span><span class="price">¥4500～</span></li>
    </ul>
    <p class="menu-note">その他、生ビール、グラッパ各種、季節の果実酒、ソフトドリンクなど、各種取り揃えております。</p>
    <p class="menu-note">また、築地市場にて旬の食材を仕入れ、ワインに合うお食事を日替わりにてご用意しております。</p>
  </section>

  <p class="tagline">ワインとお食事 “ヴェルモン”</p>

  <p class="phone">
    <svg width="60" height="48" viewBox="0 0 60 48" aria-label="電話">
      <path d="M4 14C4 6 16 4 30 4S56 6 56 14V19H42V12H18V19H4Z" fill="currentColor"/>
      <path d="M14 22H46L52 44H8Z" fill="currentColor"/>
      <circle cx="30" cy="33" r="6" fill="var(--wine)"/>
    </svg>
    <span>090-4827-3365</span>
  </p>
</main>
</body>
</html>
```